The Harbourline Aid Trust needs a graphic of their innovation approach

What we need?
- we have designed a new innovation approach (see attached). An innovation approach is the process one goes through in order to design and launch a new product or service.
- This new graphic will be used in meetings to help others understand what innovation is and how we do it. It will also be used in training sessions and be the starting point for innovation training materials we are creating
- We have created this draft graphic by copying and pasting new words over another charities innovation process
- We would like you to use your design magic and create our very own innovation process graphic. We would like it to be neat, simple, non fussy, easy to understand /read and in line with our brand colours
Attached:
1. PowerPoint:
- Slide 1: our innovation process
- Slide 2 explanation of process to bring it to life
- Slide 3&4: brand colours
- Slide 5: inspiration / examples of other processes we like the look of
2. Typeface brand guidelines
We can't wait to see what you come up with! Thank you :)
internal employees
Charity

```html
<!DOCTYPE html>
<html lang="en">
<head>
<meta charset="utf-8">
<title>Innovation Approach — The Harbourline Aid Trust</title>
<link href="https://fonts.googleapis.com/css2?family=Oswald:wght@600&family=Montserrat:wght@500;600;700&display=swap" rel="stylesheet">
<style>
  :root {
    --discover-red: #ee4130;
    --define-yellow: #f0af47;
    --deliver-blue: #218bb3;
    --iterate-coral: #f2836a;
    --iterate-sand: #f5c785;
    --ink: #231f20;
    --ink-soft: #4a4a4a;
    --paper: #ffffff;
    --paper-edge: #e4e4e4;
  }
  html, body {
    margin: 0;
    padding: 0;
    width: 1200px;
    height: 1032px;
    overflow: hidden;
  }
  .process-canvas {
    width: 1200px;
    height: 1032px;
    background: radial-gradient(ellipse at 50% 50%, var(--paper) 55%, var(--paper-edge) 100%);
  }
  .process-graphic { display: block; width: 1200px; height: 1032px; }
  .phase-label {
    font-family: "Oswald", "Arial Narrow", sans-serif;
    font-weight: 600;
    font-size: 52px;
    fill: var(--paper);
    text-anchor: middle;
  }
  .stage-label {
    font-family: "Montserrat", Arial, sans-serif;
    font-weight: 600;
    font-size: 24px;
    fill: var(--ink);
    text-anchor: middle;
  }
  .flow-label {
    font-family: "Montserrat", Arial, sans-serif;
    font-weight: 700;
    font-size: 28px;
    fill: var(--paper);
    letter-spacing: 1px;
  }
  .flow-label.small { font-size: 22px; letter-spacing: 0; }
  .loop-label {
    font-family: "Montserrat", Arial, sans-serif;
    font-weight: 500;
    font-size: 25px;
    fill: var(--ink-soft);
  }
  .loop-label.pair { font-size: 23px; }
  .stage-ring { fill: var(--paper); stroke-width: 16; }
  .ring-red { stroke: var(--discover-red); }
  .ring-yellow { stroke: var(--define-yellow); }
  .ring-blue { stroke: var(--deliver-blue); }
  .band { fill: none; stroke-width: 46; }
  .loop { fill: none; stroke-width: 7; stroke-linecap: round; }
</style>
</head>
<body>
<main class="process-canvas">
<svg class="process-graphic" viewBox="0 0 1539 1324" xmlns="http://www.w3.org/2000/svg" aria-label="Innovation approach: Discover, Define, Deliver">
  <defs>
    <linearGradient id="improvement-fade" x1="0" y1="0" x2="0" y2="1">
      <stop offset="0" stop-color="#7f9fb0"/>
      <stop offset="1" stop-color="#f0c07a"/>
    </linearGradient>
    <path id="path-insight" d="M410,385 Q305,520 300,690"/>
    <path id="path-ideate" d="M345,940 Q420,1095 605,1150"/>
    <path id="path-ideate-text" d="M358,962 L436,1056"/>
    <path id="path-test" d="M885,1130 Q1090,1080 1163,1000"/>
    <path id="path-delivery" d="M1240,750 Q1250,560 1168,440"/>
    <path id="path-iterate-left" d="M362,708 Q362,560 440,462"/>
    <path id="path-iterate-bottom-left" d="M440,945 Q520,1040 650,1090"/>
    <path id="path-iterate-bottom-right" d="M895,1085 Q1020,1030 1100,940"/>
    <path id="path-improvement" d="M1097,455 Q1170,560 1180,700"/>
  </defs>

  <!-- Phase pie -->
  <g class="phase-pie">
    <path d="M768,700 L768,395 A305,305 0 0 0 552,916 Z" fill="var(--discover-red)" stroke="var(--paper)" stroke-width="6"/>
    <path d="M772,700 L772,395 A305,305 0 0 1 1077,700 Z" fill="var(--deliver-blue)" stroke="var(--paper)" stroke-width="6"/>
    <path d="M768,704 L1073,704 A305,305 0 0 1 552,920 Z" fill="var(--define-yellow)" stroke="var(--paper)" stroke-width="6"/>
    <text class="phase-label" x="612" y="702">DISCOVER</text>
    <text class="phase-label" x="905" y="637">DELIVER</text>
    <text class="phase-label" x="847" y="835">DEFINE</text>
  </g>

  <!-- Flow bands -->
  <g class="flow-bands">
    <path class="band" d="M965,248 C880,215 825,195 825,132" stroke="var(--deliver-blue)"/>
    <polygon points="757,137 893,137 825,68" fill="var(--deliver-blue)"/>

    <use href="#path-insight" class="band" stroke="var(--discover-red)"/>
    <polygon points="256,672 346,672 301,728" fill="var(--discover-red)"/>
    <text class="flow-label" dy="10"><textPath href="#path-insight" startOffset="50%" text-anchor="middle">INSIGHT</textPath></text>

    <use href="#path-ideate" class="band" stroke="var(--define-yellow)"/>
    <path class="band" d="M345,940 Q378.75,1009.75 434.8,1059" stroke="var(--discover-red)"/>
    <polygon points="592,1112 652,1150 586,1182" fill="var(--define-yellow)"/>
    <text class="flow-label small" dy="8"><textPath href="#path-ideate-text" startOffset="50%" text-anchor="middle">IDEATE</textPath></text>
    <text class="flow-label small" dy="8"><textPath href="#path-ideate" startOffset="72%" text-anchor="middle">(IN)VALIDATE</textPath></text>

    <use href="#path-test" class="band" stroke="var(--define-yellow)"/>
    <polygon points="1104,966 1168,953 1168,1024" fill="var(--define-yellow)"/>
    <text class="flow-label" dy="10"><textPath href="#path-test" startOffset="52%" text-anchor="middle">TEST</textPath></text>

    <use href="#path-delivery" class="band" stroke="var(--deliver-blue)"/>
    <polygon points="1128,468 1190,412 1207,470" fill="var(--deliver-blue)"/>
    <text class="flow-label" dy="10" font-size="26"><textPath href="#path-delivery" startOffset="50%" text-anchor="middle">DELIVERY PLAN</textPath></text>
  </g>

  <!-- Iteration loops -->
  <g class="iteration-loops">
    <use href="#path-iterate-left" class="loop" stroke="var(--iterate-coral)"/>
    <polygon points="424,468 446,448 453,484" fill="var(--iterate-coral)"/>
    <text class="loop-label" dy="-14"><textPath href="#path-iterate-left" startOffset="55%" text-anchor="middle">Iterate</textPath></text>

    <use href="#path-iterate-bottom-left" class="loop" stroke="var(--iterate-coral)"/>
    <polygon points="436,934 462,948 432,966" fill="var(--iterate-coral)"/>
    <text class="loop-label" dy="-14"><textPath href="#path-iterate-bottom-left" startOffset="50%" text-anchor="middle">Iterate</textPath></text>

    <use href="#path-iterate-bottom-right" class="loop" stroke="var(--iterate-sand)"/>
    <polygon points="888,1088 914,1068 918,1098" fill="var(--iterate-sand)"/>
    <text class="loop-label" dy="-14"><textPath href="#path-iterate-bottom-right" startOffset="50%" text-anchor="middle">Iterate</textPath></text>

    <use href="#path-improvement" class="loop" stroke="url(#improvement-fade)"/>
    <polygon points="1162,672 1198,672 1180,704" fill="#f0c07a"/>
    <text class="loop-label pair" dy="28"><textPath href="#path-improvement" startOffset="50%" text-anchor="middle">Continuous</textPath></text>
    <text class="loop-label pair" dy="56"><textPath href="#path-improvement" startOffset="50%" text-anchor="middle">Improvement</textPath></text>
  </g>

  <!-- Stage rings -->
  <g class="stage challenge">
    <circle class="stage-ring ring-red" cx="515" cy="350" r="110"/>
    <rect role="img" aria-label="Icon: head with a question mark" x="478" y="272" width="80" height="98" rx="34" fill="var(--discover-red)"/>
    <text class="stage-label" x="513" y="406">Challenge</text>
  </g>
  <g class="stage opportunity">
    <circle class="stage-ring ring-red" cx="357" cy="835" r="110"/>
    <rect role="img" aria-label="Icon: hand holding a document" x="300" y="758" width="100" height="92" rx="12" fill="var(--discover-red)"/>
    <text class="stage-label" x="357" y="878" font-size="22">Opportunity</text>
    <text class="stage-label" x="357" y="903" font-size="22">Statement</text>
  </g>
  <g class="stage concepts">
    <circle class="stage-ring ring-yellow" cx="768" cy="1135" r="110"/>
    <rect role="img" aria-label="Icon: head with a light bulb" x="726" y="1065" width="84" height="100" rx="34" fill="var(--define-yellow)"/>
    <text class="stage-label" x="768" y="1195">Concepts</text>
  </g>
  <g class="stage solution">
    <circle class="stage-ring ring-yellow" cx="1180" cy="835" r="110"/>
    <rect role="img" aria-label="Icon: hands holding a light bulb" x="1134" y="764" width="94" height="104" rx="20" fill="var(--define-yellow)"/>
    <text class="stage-label" x="1180" y="902">Solution</text>
  </g>
  <g class="stage launch">
    <circle class="stage-ring ring-blue" cx="1023" cy="350" r="110"/>
    <rect role="img" aria-label="Icon: rocket outline" x="980" y="288" width="88" height="86" rx="18" fill="none" stroke="var(--deliver-blue)" stroke-width="5"/>
    <text class="stage-label" x="1023" y="409">Launch</text>
  </g>
</svg>
</main>
</body>
</html>
```